Environmental law firm Biz cards and stationery
Law Offices of Wendell T. Haverbrook, P.C.
Simple
Wendell T. Haverbrook
742 Dunmore Boulevard
Suite 312
Northbrook, Illinois 60062
847-555-0193 x 14
wth@haverbrooklegal.example
www.haverbrooklegal.example
I wish to use the logo that appears on my website, except for the color, which I prefer to be either black or navy blue. However, I am not opposed to using the variant of the logo showing the tree centered on top, rather than to the side. It depends on the overall appearance. Also, for the stationery letterhead, I prefer to have all contact information at the top of the page, rather than on the bottom. And, because new personnel may be added to the firm, please anticipate that the writer's fax and e-mail address will be added separately and thus not printed. Thank you.
I am uploading 2 files, containing variants of the logo I selected. One is oriented vertically, the other horizontally. Also, one has a shadow effect; the other does not.

```html
<!DOCTYPE html>
<html lang="en">
<head>
<meta charset="utf-8">
<title>Haverbrook Stationery Concepts</title>
<link href="https://fonts.googleapis.com/css2?family=Libre+Baskerville:wght@400;700&family=Lato:wght@400;700&display=swap" rel="stylesheet">
<style>
:root{
  --backdrop:#4a3325;
  --navy:#2d3a55;
  --paper:#ffffff;
  --rule:#c9ccd3;
  --ink:#3a4256;
  --muted:#8a8f9b;
  --label:#d9cfc4;
  --tree:#d6d8dc;
}
*{margin:0;padding:0;box-sizing:border-box}
html,body{width:1200px;height:466px;overflow:hidden}
body{background:var(--backdrop);font-family:"Lato",sans-serif;position:relative}
.piece{position:absolute;background:var(--paper);box-shadow:0 2px 6px rgba(0,0,0,.35)}
.label{position:absolute;color:var(--label);font-size:7px;letter-spacing:1.5px;text-transform:uppercase;text-align:center}
.brand{display:flex;align-items:center;gap:4px;font-family:"Libre Baskerville",serif;color:var(--navy);font-weight:700;line-height:1.1}
.brand .mark{width:10px;height:10px;background:var(--navy);flex:none}
.brand.light{color:var(--paper)}
.brand.light .mark{background:var(--paper)}
.brand-name{font-size:5.5px;max-width:90px}
.contact{font-size:4px;color:var(--ink);line-height:1.55}
.contact .row{display:flex;align-items:center;gap:3px}
.contact .dot{width:3px;height:3px;background:var(--navy);border-radius:50%}
.footer-band{position:absolute;left:0;right:0;bottom:0;height:12px;background:var(--navy);display:flex;align-items:center;justify-content:center;color:#c8cdda;font-size:3.5px;letter-spacing:2px}
.footer-rule{position:absolute;left:14px;right:14px;bottom:22px;height:1px;background:var(--rule)}
.tree-area{position:absolute;background:radial-gradient(ellipse at 50% 40%,#e6e7ea,var(--tree));}
.flap{position:absolute;left:0;top:0;width:100%}
</style>
</head>
<body>

<div class="label" style="left:6px;top:178px;width:130px;text-align:left">Stationery Concepts</div>

<!-- Business card front -->
<section class="piece card-front" style="left:12px;top:196px;width:126px;height:76px">
  <div class="brand" style="position:absolute;left:8px;top:8px"><span class="mark" style="width:7px;height:7px"></span><span class="brand-name" style="font-size:4.5px">Law Offices of Wendell T. Haverbrook, P.C.</span></div>
  <div class="contact" style="position:absolute;left:8px;bottom:10px;font-size:3.6px">
    <div style="font-weight:700">Wendell T. Haverbrook</div>
    <div>742 Dunmore Boulevard, Suite 312</div>
    <div>Northbrook, Illinois 60062</div>
    <div>847-555-0193 x 14</div>
    <div>wth@haverbrooklegal.example</div>
  </div>
</section>
<div class="label" style="left:12px;top:276px;width:126px">Business Card Front</div>

<!-- Business card back -->
<section class="piece card-back" style="left:12px;top:300px;width:126px;height:76px;background:var(--navy)">
  <div class="brand light" style="position:absolute;left:0;right:0;top:28px;justify-content:center"><span class="mark" style="width:14px;height:14px"></span></div>
</section>
<div class="label" style="left:12px;top:380px;width:126px">Business Card Back</div>

<!-- Letterhead option 1 -->
<section class="piece letterhead" style="left:158px;top:26px;width:226px;height:394px">
  <div class="brand" style="position:absolute;left:16px;top:18px"><span class="mark"></span><span class="brand-name">Law Offices of Wendell T. Haverbrook, P.C.</span></div>
  <div class="contact" style="position:absolute;left:118px;top:14px">
    <div class="row"><span class="dot"></span>742 Dunmore Boulevard, Suite 312</div>
    <div class="row"><span class="dot"></span>Northbrook, Illinois 60062</div>
    <div class="row"><span class="dot"></span>847-555-0193 x 14</div>
    <div class="row"><span class="dot"></span>www.haverbrooklegal.example</div>
  </div>
  <div class="footer-band">WWW.HAVERBROOKLEGAL.EXAMPLE</div>
</section>
<div class="label" style="left:158px;top:428px;width:226px">Letter Head Option 1</div>

<!-- Letterhead option 2 -->
<section class="piece letterhead" style="left:402px;top:26px;width:290px;height:394px">
  <div class="brand" style="position:absolute;left:22px;top:18px"><span class="mark"></span><span class="brand-name">Law Offices of Wendell T. Haverbrook, P.C.</span></div>
  <div class="tree-area" role="img" aria-label="Faint tree watermark" style="left:80px;top:112px;width:130px;height:140px"></div>
  <div class="footer-rule"></div>
  <div class="contact" style="position:absolute;left:0;right:0;bottom:10px;text-align:center;font-size:3.6px">742 Dunmore Boulevard, Suite 312 · Northbrook, Illinois 60062 · 847-555-0193 x 14 · www.haverbrooklegal.example</div>
</section>
<div class="label" style="left:402px;top:428px;width:290px">Letter Head Option 2</div>

<!-- Envelope backs -->
<section class="piece envelope" style="left:712px;top:26px;width:478px;height:82px">
  <svg class="flap" width="478" height="60" viewBox="0 0 478 60"><path d="M0 0H478V34Q239 66 0 34Z" fill="var(--navy)"/></svg>
  <div class="brand light" style="position:absolute;left:0;right:0;top:26px;justify-content:center"><span class="mark"></span></div>
</section>
<section class="piece envelope" style="left:712px;top:114px;width:478px;height:82px">
  <svg class="flap" width="478" height="60" viewBox="0 0 478 60"><path d="M0 0H478V30L239 58L0 30Z" fill="var(--navy)"/></svg>
  <div class="brand light" style="position:absolute;left:0;right:0;top:24px;justify-content:center"><span class="mark"></span></div>
</section>
<section class="piece envelope" style="left:712px;top:202px;width:478px;height:76px">
  <svg class="flap" width="478" height="50" viewBox="0 0 478 50"><path d="M0 0H478V22L239 46L0 22Z" fill="none" stroke="var(--rule)"/></svg>
  <div class="brand" style="position:absolute;left:0;right:0;top:38px;justify-content:center"><span class="mark"></span></div>
</section>

<!-- Envelope front -->
<section class="piece envelope" style="left:712px;top:286px;width:478px;height:128px">
  <div class="brand" style="position:absolute;left:14px;top:14px"><span class="mark"></span><span class="brand-name">Law Offices of Wendell T. Haverbrook, P.C.</span></div>
  <div class="contact" style="position:absolute;left:28px;top:30px">742 Dunmore Boulevard, Suite 312<br>Northbrook, Illinois 60062</div>
  <div class="footer-band" style="height:10px">WWW.HAVERBROOKLEGAL.EXAMPLE</div>
</section>
<div class="label" style="left:712px;top:428px;width:478px">Envelope Option 1</div>

</body>
</html>
```